Business Card Design REAL ESTATE SALES PLEASE DESIGN MY CARD 2COLOR CARD WITH RED AS THE DOMINANT

MOOR PINE REALTY
TorVHA Lic# 04827316
WALTER " WALT " KOVIC Tel 510 555-0142
TorVHA Lic# 00762408 Fax 510 555-0187
Email: walt@waltkovic.example Cell 510 555-0163
48610 FERNHILL COURT UNION CITY, CA 94999

Business

WALTER " WALT " KOVIC
TEL: 510 555-0142 FAX 510 555-0187
Address: 48610 Fernhill Court Union City , CA
EMAIL ADDRESS: walt@waltkovic.example

```html
<!DOCTYPE html>
<html lang="en">
<head>
<meta charset="utf-8">
<title>Moor Pine Realty – Business Card</title>
<link rel="stylesheet" href="https://fonts.googleapis.com/css2?family=Open+Sans:wght@400;600;700&display=swap">
<style>
  :root {
    --brand-red: #cc232f;
    --charcoal: #3b3b40;
    --paper: #ffffff;
    --paper-shade: #ececec;
    --backdrop: #efe9e2;
    --ink-light: #ffffff;
  }
  * { box-sizing: border-box; margin: 0; padding: 0; }
  html, body {
    width: 1200px; height: 900px; overflow: hidden;
    background: var(--backdrop);
    font-family: "Open Sans", sans-serif;
  }
  .canvas { position: relative; width: 1200px; height: 900px; }

  .card {
    position: absolute;
    width: 540px; height: 308px;
    border-radius: 3px;
    box-shadow: 0 6px 18px rgba(0,0,0,0.18);
    overflow: hidden;
  }

  /* Front side */
  .card-front {
    left: 60px; top: 140px;
    background: var(--brand-red);
    display: flex; align-items: center; justify-content: center;
  }
  .brand-name {
    font-weight: 600;
    letter-spacing: 1px;
    white-space: nowrap;
  }
  .card-front .brand-name { color: var(--ink-light); font-size: 36px; }

  /* Back side */
  .card-back {
    left: 600px; top: 450px;
    background: var(--brand-red);
  }
  .back-top {
    position: absolute; left: 0; top: 0; width: 100%; height: 140px;
    background: linear-gradient(180deg, var(--paper) 0%, var(--paper-shade) 100%);
    display: flex; align-items: center; justify-content: center;
    padding-top: 10px;
  }
  .card-back .brand-name { color: var(--charcoal); font-size: 36px; }
  .divider {
    position: absolute; left: 0; top: 140px; width: 100%; height: 7px;
    background: var(--charcoal);
  }
  .divider-gap {
    position: absolute; left: 0; top: 147px; width: 100%; height: 4px;
    background: var(--paper);
  }

  .back-details {
    position: absolute; left: 0; top: 151px; width: 100%; bottom: 0;
    color: var(--ink-light);
    padding: 14px 24px 0;
  }
  .contact-list {
    position: absolute; right: 290px; top: 14px;
    list-style: none; text-align: right;
    font-size: 14.5px; line-height: 23px;
  }
  .contact-list li { display: flex; align-items: center; justify-content: flex-end; gap: 7px; }
  .contact-list svg { width: 12px; height: 12px; fill: var(--ink-light); flex: none; }

  .agent {
    position: absolute; left: 272px; top: 12px;
  }
  .agent-name { font-weight: 700; font-size: 15px; letter-spacing: 0.3px; margin-bottom: 6px; }
  .licence { font-weight: 600; font-size: 12.5px; line-height: 20px; }

  .address {
    position: absolute; left: 0; right: 0; bottom: 16px;
    text-align: center; font-size: 14px;
  }
</style>
</head>
<body>
<main class="canvas">

  <section class="card card-front" aria-label="Card front">
    <span class="brand-name">MOOR PINE REALTY</span>
  </section>

  <section class="card card-back" aria-label="Card back">
    <div class="back-top">
      <span class="brand-name">MOOR PINE REALTY</span>
    </div>
    <div class="divider"></div>
    <div class="divider-gap"></div>

    <div class="back-details">
      <ul class="contact-list">
        <li>510 555-0142
          <svg viewBox="0 0 24 24" aria-hidden="true"><path d="M6.6 10.8a15 15 0 0 0 6.6 6.6l2.2-2.2a1 1 0 0 1 1-.25 11.4 11.4 0 0 0 3.6.57 1 1 0 0 1 1 1V20a1 1 0 0 1-1 1A17 17 0 0 1 3 4a1 1 0 0 1 1-1h3.5a1 1 0 0 1 1 1c0 1.25.2 2.45.57 3.57a1 1 0 0 1-.25 1z"/></svg>
        </li>
        <li>510 555-0163
          <svg viewBox="0 0 24 24" aria-hidden="true"><path d="M7 1h10a2 2 0 0 1 2 2v18a2 2 0 0 1-2 2H7a2 2 0 0 1-2-2V3a2 2 0 0 1 2-2zm0 3v14h10V4zm5 15.5a1 1 0 1 0 0 2 1 1 0 0 0 0-2z"/></svg>
        </li>
        <li>510 555-0187
          <svg viewBox="0 0 24 24" aria-hidden="true"><path d="M6 2h9l3 3v4h2a2 2 0 0 1 2 2v9a2 2 0 0 1-2 2H4a2 2 0 0 1-2-2v-9a2 2 0 0 1 2-2h2zm2 2v5h8V6h-2V4zm-2 9v2h3v-2zm5 0v2h3v-2zm-5 4v2h3v-2zm5 0v2h3v-2z"/></svg>
        </li>
        <li>walt@waltkovic.example
          <svg viewBox="0 0 24 24" aria-hidden="true"><path d="M2 5h20v14H2zm2 2v.5l8 5 8-5V7l-8 5z"/></svg>
        </li>
      </ul>

      <div class="agent">
        <p class="agent-name">WALTER " WALT " KOVIC</p>
        <p class="licence">TorVHA Lic # 00762408</p>
        <p class="licence">TorVHA Lic # 04827316</p>
      </div>

      <p class="address">48610 Fernhill Court&nbsp; Union City, CA 94999</p>
    </div>
  </section>

</main>
</body>
</html>
```